someone who can choose good colours and fonts and a style for an already layed out web page

HI

We need someone who can choose good colors and fonts and style for an already layed out web page.

please look at the first file.

The hard part of what needs to go where is already done,

1) we just need a type of character suitable for our business

2) colors probably in the green / yellow spectrum to suit our business

3) we need you to choose the style. For example you could choose round photos, or square buttons, video boxes with or without frames, that sort of stuff, just tweaking of what is there. plain arial is probably what we'd like but with text but with script or memorable headings. We would just like a design style that you think would be good gor our business model.

4) the twitter,facebook logo needs to be put in a new place

our project is an Italian style village in Italy called "Casale Delle Rondini", in Abruzzo, Italy.
It is surrounded by vineyards, lake and olive trees.

The most important is that it looks expensive, the village is eco friendly so anything on those lines is great, Obviously Italian, so italian looking characters

our website is www.collinetorre.com but we are updating it. we like the style of the old site , but it is too out of date

you can create the layout using the files we've given below and boxes
Updates

hi we've just updated out brief to make it more simple, its actually not much work its just about design choices

Target Market(s)

all lovers of Italian things
eco frienly

Industry/Entity Type

Business

Font styles to use
Decorative
Script

Colors
fcf9ce
faee3f
fde18a
fece3e
cadf82
9bcb3b
acd036
fce7d2
ec2027

Requirements
Must have
• has to have the same layout or similar so as all the boxes and links are in there
twitter,facebook and other logos need to be present where you want them
Nice to have
• we have chosen some colors but you can choose others 3 or 4 are usual a good number with a light yellow background maybe....
Should not have
• no old style must look up to date

```html
<!DOCTYPE html>
<html lang="en">
<head>
<meta charset="utf-8">
<title>Casale Delle Rondini</title>
<link rel="stylesheet" href="https://fonts.googleapis.com/css2?family=Great+Vibes&family=Lora:wght@400;700&family=Playfair+Display:wght@400&display=swap">
<style>
:root{
  --wood:#f3d7a6;
  --wood-dark:#e7c48d;
  --red:#ec2027;
  --red-dark:#c3141b;
  --green-deep:#2c4a10;
  --green-mid:#4f7d18;
  --green-leaf:#9bcb3b;
  --green-lime:#acd036;
  --green-soft:#cadf82;
  --yellow:#fece3e;
  --yellow-light:#fde18a;
  --cream:#fcf9ce;
  --text:#3a3a3a;
  --muted:#6b6b6b;
  --gold:#a7891f;
  --blue-link:#3d5c7a;
  --white:#ffffff;
}
*{margin:0;padding:0;box-sizing:border-box}
html,body{width:1146px;height:1200px;overflow:hidden}
body{position:relative;background:var(--white);font-family:"Lora",Georgia,serif;color:var(--text)}
.abs{position:absolute}

/* header */
.site-header{left:0;top:0;width:1146px;height:96px;background:linear-gradient(180deg,#f6ddb0,var(--wood));border-bottom:3px solid var(--red)}
.brand{left:198px;top:22px;display:flex;align-items:center;gap:10px}
.brand-mark{width:40px;height:40px;border-radius:50%;background:var(--green-mid)}
.brand-name{font-family:"Playfair Display",Georgia,serif;font-size:24px;color:var(--red)}
.contact{right:191px;top:2px;text-align:right}
.phone{font-size:17px;color:var(--blue-link);display:flex;align-items:center;gap:3px;justify-content:flex-end}
.address{font-size:11px;color:var(--blue-link)}
.social{display:flex;gap:6px}
.social span{width:28px;height:28px;border-radius:50%;display:block}
.social .s1{background:#c9302c}.social .s2{background:#5aa4dc}.social .s3{background:#3b5ca8}
.header-social{right:191px;top:43px}
.main-nav{left:569px;top:77px;display:flex;font-size:12.5px}
.main-nav a{color:#3a3a3a;text-decoration:none;padding:2px 13px 3px;height:19px}
.main-nav a.active{background:var(--red);color:var(--white)}

/* hero */
.hero{left:0;top:96px;width:1146px;height:331px;background:radial-gradient(ellipse at 50% 100%,#7fae2a 0%,#4c7d17 45%,#2f5310 100%)}
.site-map{left:198px;top:122px;width:341px;height:276px;border:3px solid var(--green-lime);background:linear-gradient(135deg,#fbf6d6,#e9efb9 40%,#7db63a 70%,#fbf6d6)}
.map-tab{left:210px;top:120px;width:41px;height:68px}
.thumb-strip{left:556px;top:122px;width:397px;height:89px;background:var(--cream);border:1px solid var(--green-soft);display:flex;gap:3px;padding:3px 3px}
.thumb-strip div{flex:1;border:1px solid #d7de9a}
.t1{background:linear-gradient(#4c7cc5,#f0c12a)}
.t2{background:linear-gradient(#f4c88a,#c79058)}
.t3{background:linear-gradient(135deg,#2e4d9a,#e9e2d2)}
.t4{background:linear-gradient(#cfd8a0,#4f7d20)}
.t5{background:linear-gradient(#4c72c5,#b88a4e)}
.slider{left:554px;top:221px;width:401px;height:179px;background:linear-gradient(180deg,#e7b070 0%,#b9825a 45%,#5b4434 75%,#2e2620 100%)}
.slider-arrow{top:300px;width:16px;height:22px}

/* intro */
.intro-title{left:198px;top:455px;font-family:"Playfair Display",Georgia,serif;font-size:37px;color:var(--green-leaf);font-weight:400}
.intro-col{top:508px;width:362px;font-size:9px;line-height:14px;color:var(--text)}
.hero-rule{left:0;top:432px;width:1146px;border-top:1px dashed #e4e8c8}

/* feature band */
.feature-band{left:0;top:621px;width:1146px;height:181px;background:radial-gradient(ellipse at 50% 80%,#6f9c22 0%,#3e6414 35%,#2c4a10 70%)}
.newsletter{left:198px;top:648px;width:241px;height:124px;background:linear-gradient(135deg,#f25a4b,#e62227 60%,#d81b1f);box-shadow:0 2px 4px rgba(0,0,0,.3)}
.newsletter-text{left:210px;top:658px;font-family:"Great Vibes",cursive;font-size:31px;line-height:36px;color:var(--white)}
.envelope{left:347px;top:640px;width:84px;height:54px}
.seasons{left:454px;top:652px;width:241px}
.season{display:flex;align-items:center;height:29px;border-bottom:1px dashed rgba(0,0,0,.55);font-size:12.5px;color:var(--white)}
.season:last-child{border-bottom:none}
.season svg{width:20px;height:20px;margin:0 22px 0 20px}
.book-trip{left:708px;top:648px;width:241px;height:124px;background:linear-gradient(135deg,#6e9b26,#a4cb3c 50%,#88b52e);border:2px solid #b9d660}
.book-title{left:805px;top:655px;font-family:"Great Vibes",cursive;font-size:32px;color:var(--white)}
.btn-more{left:827px;top:728px;width:113px;height:32px;background:linear-gradient(#fde18a,#fece3e);border:1px solid #f0bd2f;font-size:12px;color:var(--gold);display:flex;align-items:center;justify-content:center}

/* blogs */
.section-head{top:828px;display:flex;align-items:center;gap:8px;font-family:"Playfair Display",Georgia,serif;font-size:26px;color:var(--green-leaf)}
.col-rule{top:815px;height:255px;border-left:1px solid var(--green-soft)}
.post{width:240px;height:100px}
.post-thumb{left:0;top:2px;width:50px;height:50px;background:radial-gradient(circle at 50% 40%,#f2a53a,#6b2a0c 50%,#1a0c05)}
.post-title{left:64px;top:0;font-size:9.5px;color:var(--green-leaf);white-space:nowrap}
.post-meta{left:64px;top:14px;font-family:Arial,sans-serif;font-size:6.5px;color:var(--muted)}
.post-body{left:66px;top:26px;width:175px;font-size:9.5px;line-height:14.5px;color:var(--text)}
.post-more{right:-1px;top:74px;font-size:13px;color:var(--gold)}
.video{width:114px;height:86px;background:linear-gradient(180deg,#8cc2e8 0%,#d9d0b4 40%,#3d7ea0 70%,#2c6682 100%)}
.video svg{position:absolute;left:41px;top:27px}

/* footer */
.site-footer{left:0;top:1079px;width:1146px;height:121px;background:linear-gradient(180deg,var(--wood),#f0d09c)}
.footer-nav{left:198px;top:1087px;display:flex;gap:25px;font-size:12px;color:#6d5a3a}
.footer-links{left:198px;top:1121px;width:420px;font-family:Arial,sans-serif;font-size:7px;line-height:10px;color:#3a3a3a}
.footer-bottom{left:198px;top:1185px;font-family:Arial,sans-serif;font-size:7px;color:#3a3a3a}
.footer-social{left:855px;top:1088px}
.footer-brand{left:725px;top:1134px;display:flex;align-items:center;gap:10px}
.footer-brand .brand-mark{width:44px;height:44px;background:#5a4a2a}
.footer-brand .brand-name{color:#5a4a2a;font-size:22px}
</style>
</head>
<body>

<header class="site-header abs">
  <div class="brand abs"><span class="brand-mark"></span><span class="brand-name">Casale Delle Rondini</span></div>
  <div class="contact abs">
    <div class="phone"><svg width="13" height="13" viewBox="0 0 16 16"><path d="M4 1l3 3-2 2c1 2 3 4 5 5l2-2 3 3-2 3C7 14 2 9 1 3z" fill="var(--red)"/></svg>0851234567</div>
    <div class="address">Via dei Mandorli 12 Torrevecchia</div>
  </div>
  <div class="social header-social abs"><span class="s1"></span><span class="s2"></span><span class="s3"></span></div>
  <nav class="main-nav abs">
    <a class="active">Description</a><a>Wich Reason</a><a>Price List</a><a>Example</a><a>Contact</a>
  </nav>
</header>

<section class="hero abs"></section>
<div class="site-map abs" role="img" aria-label="Site plan of the village phases with olive groves, lake, pool and park"></div>
<svg class="map-tab abs" viewBox="0 0 41 68"><path d="M0 0h41v60l-20.5-8L0 60z" fill="var(--red)"/><circle cx="19" cy="28" r="7" fill="none" stroke="var(--yellow-light)" stroke-width="3"/><path d="M24 33l6 6" stroke="var(--yellow-light)" stroke-width="3.5" stroke-linecap="round"/></svg>
<div class="thumb-strip abs">
  <div class="t1" role="img" aria-label="Sunflower photo"></div>
  <div class="t2" role="img" aria-label="Child on a sunset beach photo"></div>
  <div class="t3" role="img" aria-label="Snowy mountain slope photo"></div>
  <div class="t4" role="img" aria-label="Olive grove photo"></div>
  <div class="t5" role="img" aria-label="Roman amphitheatre photo"></div>
</div>
<div class="slider abs" role="img" aria-label="Slideshow photo of a canal bridge at sunset"></div>
<svg class="slider-arrow abs" style="left:558px" viewBox="0 0 16 22"><path d="M13 2L4 11l9 9" fill="none" stroke="var(--red)" stroke-width="4"/></svg>
<svg class="slider-arrow abs" style="left:935px" viewBox="0 0 16 22"><path d="M3 2l9 9-9 9" fill="none" stroke="var(--red)" stroke-width="4"/></svg>

<div class="hero-rule abs"></div>
<h1 class="intro-title abs">Casale delle Rondini</h1>
<p class="intro-col abs" style="left:198px">Is built in traditional Italian architectural style and surrounded by olive groves, vineyards, a beautiful lake surrounded by a park with wildlife. The panoramic view of the mountains is breathtaking and you can see for 30 miles on a clear day. Red and white umbrellas, barbeques, swimming pools and a spa will contribute to its unique atmosphere. there will also be a health farm, where you can treat yourself to a luxurious massage.</p>
<p class="intro-col abs" style="left:583px">Ten shops and ensure any of your other needs can be met. Casale delle Rondini is ensconced in the beauty of the Italian countryside, where the hot white sandy beaches of the Adriatic coastline meet the cold snowy ski-slopes of the Appenine mountains, with Rome only a short car ride away.<br>Each property will be in the OLD Abruzzo style, with attractive brick and stone walls. There are one-, two- and three-bedroomed apartments and three- or four-bedroomed villas.</p>

<section class="feature-band abs"></section>
<div class="newsletter abs" role="img" aria-label="Red toned photo of trees behind the newsletter signup"></div>
<div class="newsletter-text abs">Sign Up<br>&nbsp;&nbsp;for Newsletter</div>
<div class="envelope abs" role="img" aria-label="Envelope illustration" style="background:linear-gradient(#f7e6c8,#f5b54a)"></div>
<div class="seasons abs">
  <div class="season"><svg viewBox="0 0 20 20"><path d="M10 12c-4 0-6-3-6-8l3 2 3-4 3 4 3-2c0 5-2 8-6 8zM10 12v7" fill="#fff" stroke="#fff" stroke-width="1.5"/></svg>Photos of Spring</div>
  <div class="season"><svg viewBox="0 0 20 20"><circle cx="10" cy="10" r="4" fill="none" stroke="#fff" stroke-width="2"/><path d="M10 1v3M10 16v3M1 10h3M16 10h3M4 4l2 2M14 14l2 2M16 4l-2 2M4 16l2-2" stroke="#fff" stroke-width="2"/></svg>Photos of Summer</div>
  <div class="season"><svg viewBox="0 0 20 20"><path d="M10 1l3 5 5-1-2 5 3 3-5 1v4l-4-3-4 3v-4l-5-1 3-3-2-5 5 1z" fill="#fff"/></svg>Photos of Autumn</div>
  <div class="season"><svg viewBox="0 0 20 20"><path d="M10 1v18M2 5.5l16 9M2 14.5l16-9M7 2l3 3 3-3M7 18l3-3 3 3" fill="none" stroke="#fff" stroke-width="1.8"/></svg>Photos of Winter</div>
</div>
<div class="book-trip abs" role="img" aria-label="Green photo of a countryside path"></div>
<div class="book-title abs">Book Trip</div>
<div class="btn-more abs">Read more</div>

<div class="section-head abs" style="left:198px"><svg width="34" height="26" viewBox="0 0 34 26"><path d="M0 2h34v16H12l-6 7v-7H0z" fill="var(--red)"/></svg>Old Blog</div>
<div class="col-rule abs" style="left:445px"></div>
<div class="section-head abs" style="left:456px"><svg width="34" height="26" viewBox="0 0 34 26"><path d="M0 2h34v16H12l-6 7v-7H0z" fill="var(--red)"/></svg>New Blog</div>
<div class="col-rule abs" style="left:700px"></div>
<div class="section-head abs" style="left:707px"><svg width="32" height="32" viewBox="0 0 32 32"><circle cx="16" cy="16" r="16" fill="var(--red)"/><path d="M12 9l11 7-11 7z" fill="#fff"/></svg>Videos</div>

<div class="post abs" style="left:198px;top:879px"><div class="post-thumb abs" role="img" aria-label="Festival torches photo"></div><div class="post-title abs">The Farchie Festival in Fara Filiorum Petri</div><div class="post-meta abs">3 January 2014 &nbsp;Posted by — Giulia @ 9:57 am</div><p class="post-body abs">The Farchie Festival, is held each year, on the 16th of January, in Fara Filiorum Petri, a small town located in the ...</p><div class="post-more abs">Read more</div></div>
<div class="post abs" style="left:198px;top:979px"><div class="post-thumb abs" role="img" aria-label="Festival torches photo"></div><div class="post-title abs">The Farchie Festival in Fara Filiorum Petri</div><div class="post-meta abs">3 January 2014 &nbsp;Posted by — Giulia @ 9:57 am</div><p class="post-body abs">The Farchie Festival, is held each year, on the 16th of January, in Fara Filiorum Petri, a small town located in the ...</p><div class="post-more abs">Read more</div></div>
<div class="post abs" style="left:456px;top:879px"><div class="post-thumb abs" role="img" aria-label="Festival torches photo"></div><div class="post-title abs">The Farchie Festival in Fara Filiorum Petri</div><div class="post-meta abs">3 January 2014 &nbsp;Posted by — Giulia @ 9:57 am</div><p class="post-body abs">The Farchie Festival, is held each year, on the 16th of January, in Fara Filiorum Petri, a small town located in the ...</p><div class="post-more abs">Read more</div></div>
<div class="post abs" style="left:456px;top:979px"><div class="post-thumb abs" role="img" aria-label="Festival torches photo"></div><div class="post-title abs">The Farchie Festival in Fara Filiorum Petri</div><div class="post-meta abs">3 January 2014 &nbsp;Posted by — Giulia @ 9:57 am</div><p class="post-body abs">The Farchie Festival, is held each year, on the 16th of January, in Fara Filiorum Petri, a small town located in the ...</p><div class="post-more abs">Read more</div></div>

<div class="video abs" style="left:708px;top:873px" role="img" aria-label="Canal video thumbnail"><svg width="32" height="32" viewBox="0 0 32 32"><circle cx="16" cy="16" r="15" fill="rgba(255,255,255,.45)"/><path d="M12 9l11 7-11 7z" fill="rgba(255,255,255,.8)"/></svg></div>
<div class="video abs" style="left:835px;top:873px" role="img" aria-label="Canal video thumbnail"><svg width="32" height="32" viewBox="0 0 32 32"><circle cx="16" cy="16" r="15" fill="rgba(255,255,255,.45)"/><path d="M12 9l11 7-11 7z" fill="rgba(255,255,255,.8)"/></svg></div>
<div class="video abs" style="left:708px;top:974px" role="img" aria-label="Canal video thumbnail"><svg width="32" height="32" viewBox="0 0 32 32"><circle cx="16" cy="16" r="15" fill="rgba(255,255,255,.45)"/><path d="M12 9l11 7-11 7z" fill="rgba(255,255,255,.8)"/></svg></div>
<div class="video abs" style="left:835px;top:974px" role="img" aria-label="Canal video thumbnail"><svg width="32" height="32" viewBox="0 0 32 32"><circle cx="16" cy="16" r="15" fill="rgba(255,255,255,.45)"/><path d="M12 9l11 7-11 7z" fill="rgba(255,255,255,.8)"/></svg></div>

<footer class="site-footer abs"></footer>
<nav class="footer-nav abs"><span>Description</span><span>Wich Reason</span><span>Price List</span><span>Example</span><span>Contact</span></nav>
<p class="footer-links abs">Find more houses, land, properties for sale and real estate on the following sites:<br>HomesAcrossFlorida (ita)HomesAcrossFlorida (uk)HomesAcrossFlorida (es)HomesAcrossFlorida (de)HomesAcrossItaly<br>(en)HomesAcrossItaly(ita)HomesAcrossItaly (bg)HomesAcrossItaly (ru)HomesAcrossItaly (de)Casale Delle Rondini (uk)</p>
<p class="footer-bottom abs">Casale Delle Rondini (ita)Casale Delle Rondini (de)Garden Pools Tampa FairwayHomesSale Italianvillasforsale</p>
<div class="social footer-social abs"><span class="s1"></span><span class="s2"></span><span class="s3"></span></div>
<div class="footer-brand abs"><span class="brand-mark"></span><span class="brand-name">Casale Delle Rondini</span></div>

</body>
</html>
```